Awesome Dessert Baker needs Sticker Design

My wife is an incredible baker. She specializes in desserts and everyone that tastes her baked goods has told her to start selling them. She recently decided to go into business and just through word of mouth and her reputation she is already getting steady orders.

She is looking to have a sticker developed to put on her cake boxes and packaging.

She wants the following:
1. Colors to be used- hot pink, purple, white
2. Want a sleek, modern design and style incorporating following:
name: Whisked by Nola
tel: 917 555 0148
email: nola@whiskedbynola.example

**no old fashion baking references like rolling pins, aprons, ect.

We want the sticker to be very appealing and eye catching that will further promote her image and business.

Industry/Entity Type

Fashion

Requirements
Must have
• Must contain the following information:

Whisked by Nola
917 555 0148 (please make small and discreet)
nola@whiskedbynola.example (please make small and discreet)
Should not have
• **no old fashion baking references like rolling pins, aprons, ect.

```html
<!DOCTYPE html>
<html lang="en">
<head>
<meta charset="utf-8">
<title>Whisked by Nola — Sticker</title>
<link rel="stylesheet" href="https://fonts.googleapis.com/css2?family=PT+Sans:wght@400;700&display=swap">
<style>
  :root {
    --backdrop: #ad40c9;
    --sticker-black: #000000;
    --doily-white: #ffffff;
    --ribbon-purple: #ad3dcb;
    --ribbon-fold: #6e1f85;
    --ribbon-text: #ffffff;
    --brand-ink: #000000;
  }
  html, body {
    margin: 0;
    padding: 0;
    width: 1200px;
    height: 900px;
    overflow: hidden;
    background: var(--backdrop);
  }
  .sticker-canvas {
    display: block;
    width: 1200px;
    height: 900px;
  }
  .sticker-base { fill: var(--sticker-black); }
  .doily { fill: var(--doily-white); }
  .brand-name {
    font-family: "PT Sans", sans-serif;
    fill: var(--brand-ink);
    text-anchor: middle;
  }
  .brand-name__small { font-size: 50px; letter-spacing: 2px; }
  .brand-name__large { font-size: 118px; letter-spacing: 12px; }
  .ribbon { fill: var(--ribbon-purple); }
  .ribbon-fold { fill: var(--ribbon-fold); }
  .ribbon-text {
    font-family: "PT Sans", sans-serif;
    font-weight: 700;
    fill: var(--ribbon-text);
    text-anchor: middle;
  }
  .ribbon-text--phone { font-size: 30px; letter-spacing: 5px; }
  .ribbon-text--email { font-size: 27px; letter-spacing: 1.5px; }
</style>
</head>
<body>
<svg class="sticker-canvas" viewBox="0 0 1200 900" xmlns="http://www.w3.org/2000/svg">
  <circle class="sticker-base" cx="600" cy="450" r="350"/>

  <circle class="doily" cx="606" cy="442" r="294" role="img" aria-label="White paper lace doily with scalloped edge and cut-out pattern"/>

  <text class="brand-name brand-name__small" x="600" y="405">WHISKED BY</text>
  <text class="brand-name brand-name__large" x="606" y="518">NOLA</text>

  <g class="contact-ribbons" transform="rotate(-15 630 600)">
    <polygon class="ribbon-fold" points="896,622 920,622 920,607"/>
    <rect class="ribbon" x="392" y="622" width="528" height="50"/>
    <text class="ribbon-text ribbon-text--email" x="656" y="656">nola@whiskedbynola.example</text>

    <polygon class="ribbon-fold" points="904,556 932,556 932,528"/>
    <polygon class="ribbon-fold" points="322,606 350,606 350,628"/>
    <rect class="ribbon" x="322" y="556" width="610" height="50"/>
    <text class="ribbon-text ribbon-text--phone" x="632" y="592">917 555 0148</text>
  </g>
</svg>
</body>
</html>
```